PGA Nashville 2025

a catchy design to use on instagram and email to market my upcoming dental course called Prosthetic Guided Alignment coming up May 23-24 in Nashville at the Tamberlynne . the course is a " 2-day Hands On Workshop" in the uploaded files are some of the ideas we made ourselves in the past but they don't look professional. i also included other peoples post that i like.

```html
<!DOCTYPE html>
<html lang="en">
<head>
<meta charset="utf-8">
<title>PGA Nashville 2025</title>
<link href="https://fonts.googleapis.com/css2?family=Montserrat:wght@500;600;700;800&display=swap" rel="stylesheet">
<style>
  :root{
    --sky:#0fb4ef;
    --navy:#1d3b80;
    --deep:#17336f;
    --white:#ffffff;
    --yellow:#fff21a;
    --photo-a:#e9a59c;
    --photo-b:#c55f5a;
    --ink:#0b0f1c;
  }
  *{margin:0;padding:0;box-sizing:border-box}
  html,body{width:916px;height:1200px;overflow:hidden;background:var(--deep)}
  .poster{
    position:relative;width:916px;height:1200px;overflow:hidden;
    font-family:"Montserrat",sans-serif;color:var(--white);
    background:linear-gradient(105deg,var(--sky) 0%,#1479c4 45%,var(--navy) 100%);
  }
  .venue-backdrop{
    position:absolute;left:0;top:560px;width:916px;height:640px;
    background:linear-gradient(180deg,rgba(255,255,255,0) 0%,rgba(180,215,240,.18) 45%,rgba(40,170,230,.35) 100%);
  }
  .brand{position:absolute;left:270px;top:36px;display:flex;align-items:center;gap:16px}
  .brand-name{font-weight:800;font-size:58px;letter-spacing:1px;line-height:1;color:var(--ink)}
  .brand-tagline{font-weight:500;font-size:20px;line-height:24px;color:var(--white)}
  .photo-frame{
    position:absolute;left:66px;top:150px;width:770px;height:417px;
    border:2px solid var(--white);border-radius:76px;
  }
  .photo{
    position:absolute;left:76px;top:121px;width:764px;height:436px;border-radius:76px;
    background:radial-gradient(ellipse at 55% 50%,#f3ece4 0%,#d88c84 35%,var(--photo-b) 60%,var(--photo-a) 100%);
  }
  .course-title{
    position:absolute;left:0;top:624px;width:916px;text-align:center;
    font-weight:600;font-size:41px;line-height:48px;letter-spacing:.5px;
  }
  .coming-up{position:absolute;left:0;top:740px}
  .details{
    position:absolute;left:108px;top:880px;width:699px;height:132px;
    border:2px solid var(--white);border-radius:66px;
  }
  .calendar{position:absolute;left:46px;top:34px}
  .date{position:absolute;left:135px;top:22px;font-weight:800;font-size:41px;line-height:41px}
  .divider{position:absolute;left:274px;top:14px;width:2px;height:100px;background:var(--white)}
  .pin{position:absolute;left:301px;top:38px}
  .location{
    position:absolute;left:358px;top:37px;font-weight:700;font-size:27px;line-height:31px;color:var(--yellow);
  }
  .format{position:absolute;left:0;top:1062px;width:916px;text-align:center}
  .format-lead{font-weight:500;font-size:27px;line-height:34px}
  .format-main{font-weight:800;font-size:40px;line-height:48px;letter-spacing:.5px}
</style>
</head>
<body>
<div class="poster">
  <div class="venue-backdrop" role="img" aria-label="Faint view of the Tamberlynne hotel poolside and Nashville skyline"></div>

  <div class="brand">
    <span class="brand-name">PGA</span>
    <span class="brand-tagline">Prosthetic Guided<br>Alignment</span>
  </div>

  <div class="photo-frame"></div>
  <div class="photo" role="img" aria-label="Close-up of a smile with pink orthodontic braces and elastics"></div>

  <h1 class="course-title">PROSTHETIC GUIDED<br>ALIGNMENT</h1>

  <svg class="coming-up" width="916" height="110" viewBox="0 0 916 110" aria-label="Coming up">
    <defs>
      <filter id="outline-text" x="-5%" y="-20%" width="110%" height="140%">
        <feMorphology in="SourceAlpha" operator="dilate" radius="2.5" result="grown"/>
        <feComposite in="grown" in2="SourceAlpha" operator="out" result="ring"/>
        <feFlood flood-color="#ffffff"/>
        <feComposite in2="ring" operator="in"/>
      </filter>
    </defs>
    <text x="133" y="92" textLength="649" lengthAdjust="spacingAndGlyphs"
      font-family="Montserrat, sans-serif" font-weight="600" font-size="108"
      fill="#ffffff" filter="url(#outline-text)">COMING UP</text>
  </svg>

  <div class="details">
    <svg class="calendar" width="62" height="62" viewBox="0 0 62 62" fill="none" stroke="#fff" stroke-width="3.5" aria-hidden="true">
      <rect x="3" y="8" width="48" height="48" rx="7"/>
      <line x1="3" y1="20" x2="51" y2="20"/>
      <line x1="15" y1="3" x2="15" y2="13"/><line x1="27" y1="3" x2="27" y2="13"/><line x1="39" y1="3" x2="39" y2="13"/>
      <g fill="#fff" stroke="none">
        <circle cx="13" cy="29" r="2.2"/><circle cx="22" cy="29" r="2.2"/><circle cx="31" cy="29" r="2.2"/><circle cx="40" cy="29" r="2.2"/>
        <circle cx="13" cy="38" r="2.2"/><circle cx="22" cy="38" r="2.2"/>
        <circle cx="13" cy="47" r="2.2"/><circle cx="22" cy="47" r="2.2"/>
      </g>
      <circle cx="46" cy="47" r="13" fill="#1676c2"/>
      <polyline points="46,40 46,47 51,50"/>
    </svg>
    <div class="date">MAY<br>23-24</div>
    <div class="divider"></div>
    <svg class="pin" width="46" height="60" viewBox="0 0 46 60" aria-hidden="true">
      <path d="M23 0C10 0 0 10 0 23c0 16 23 37 23 37s23-21 23-37C46 10 36 0 23 0z" fill="#fff21a"/>
      <circle cx="23" cy="22" r="9" fill="#1a5fb0"/>
    </svg>
    <div class="location">IN NASHVILLE AT<br>THE TAMBERLYNNE</div>
  </div>

  <div class="format">
    <p class="format-lead">THE COURSE IS A</p>
    <p class="format-main">2-DAY HANDS ON WORKSHOP</p>
  </div>
</div>
</body>
</html>
```